Reed & Vale NC grand opening (for BILLBOARD)

Advertising the grand opening of our cannabis/hemp shop in NC. We will sell all things hemp (flower, cartridges, disposables, edibles, creams, lotions, pet products etc...)

Requirements
Must have
• include, open starting Aug 1, but grand opening Aug 15th.
Nice to have
• Difference slogan ideas "Save some cash, buy our grass" "Find your perfect high at Reed & Vale cannabis store" "Experience Nature's Gift: Reed & Vale Cannabis Store"

```html
<!DOCTYPE html>
<html lang="en">
<head>
<meta charset="utf-8">
<title>Reed &amp; Vale — Grand Opening Billboard</title>
<link rel="stylesheet" href="https://fonts.googleapis.com/css2?family=Anton&family=Kaushan+Script&family=Poppins:wght@600;700;800&display=swap">
<style>
  :root {
    --page-bg: #f4f5f7;
    --white: #ffffff;
    --green: #6fc73a;
    --green-light: #96e05a;
    --green-deep: #4fa823;
    --navy: #13134a;
    --navy-dark: #0b0b33;
    --divider: rgba(40, 70, 20, 0.55);
    --edge: #c9cdd6;
  }
  * { box-sizing: border-box; margin: 0; padding: 0; }
  html, body {
    width: 960px;
    height: 1200px;
    overflow: hidden;
    background: var(--page-bg);
  }
  .billboard {
    position: absolute;
    left: 40px;
    top: 417px;
    width: 880px;
    height: 366px;
    overflow: hidden;
    background: var(--white);
    box-shadow: 0 10px 28px rgba(0, 0, 0, 0.14);
    font-family: 'Poppins', sans-serif;
  }
  .green-field {
    position: absolute;
    inset: 0;
    background: radial-gradient(ellipse at 62% 45%, var(--green-light) 0%, var(--green) 48%, var(--green-deep) 100%);
    clip-path: polygon(358px 0, 880px 0, 880px 366px, 237px 366px);
  }
  .field-edge {
    position: absolute;
    inset: 0;
    width: 880px;
    height: 366px;
  }

  /* Brand block */
  .brand {
    position: absolute;
    left: 46px;
    top: 34px;
    display: flex;
    align-items: center;
    gap: 10px;
    font-weight: 700;
    font-size: 38px;
    line-height: 1;
    color: var(--navy);
    white-space: nowrap;
  }
  .brand-dot {
    width: 16px;
    height: 16px;
    border-radius: 50%;
    background: var(--green-deep);
  }
  .open-dates {
    position: absolute;
    left: 48px;
    top: 80px;
    font-size: 12px;
    font-weight: 700;
    letter-spacing: 0.3px;
    line-height: 1.3;
    color: var(--green-deep);
    text-transform: uppercase;
    white-space: nowrap;
  }
  .open-dates strong { color: var(--navy); font-weight: 700; }

  /* Photo area: woman with megaphone */
  .promo-photo {
    position: absolute;
    left: 20px;
    top: 110px;
    width: 378px;
    height: 256px;
    border-radius: 90px 90px 0 0;
    background: linear-gradient(90deg, #d8c1ad 0%, #ece6e0 30%, #b83a44 46%, #c9444d 54%, #efebe6 70%, #e2ded9 100%);
  }
  .megaphone-strokes {
    position: absolute;
    left: 392px;
    top: 254px;
    width: 42px;
    height: 28px;
  }

  /* Headline */
  .headline-script {
    position: absolute;
    left: 425px;
    top: 14px;
    font-family: 'Kaushan Script', cursive;
    font-size: 88px;
    line-height: 1;
    color: var(--white);
    text-shadow: 0 2px 0 rgba(40, 90, 20, 0.35);
  }
  .headline-main {
    position: absolute;
    left: 474px;
    top: 82px;
    font-family: 'Anton', sans-serif;
    font-size: 100px;
    line-height: 1;
    letter-spacing: 2px;
    color: var(--navy);
    text-shadow: 0 3px 2px rgba(0, 0, 0, 0.25);
  }
  .accent-strokes {
    position: absolute;
    left: 690px;
    top: 34px;
    width: 52px;
    height: 40px;
  }
  .divider {
    position: absolute;
    left: 428px;
    top: 178px;
    width: 428px;
    height: 2px;
    background: linear-gradient(90deg, transparent, var(--divider) 12%, var(--divider) 88%, transparent);
  }

  /* Product list */
  .product-list {
    position: absolute;
    list-style: none;
    display: flex;
    font-size: 13px;
    font-weight: 700;
    letter-spacing: 0.3px;
    line-height: 1;
    color: var(--navy);
    text-transform: uppercase;
    white-space: nowrap;
  }
  .product-list li {
    display: flex;
    align-items: center;
    gap: 5px;
  }
  .product-list li::before {
    content: "";
    width: 7px;
    height: 7px;
    border-radius: 50%;
    background: var(--white);
  }
  .product-list--top { left: 428px; top: 216px; gap: 14px; }
  .product-list--bottom { left: 454px; top: 250px; gap: 24px; }

  /* Phone */
  .phone-pill {
    position: absolute;
    left: 426px;
    top: 300px;
    width: 402px;
    height: 40px;
    border-radius: 20px;
    background: var(--navy-dark);
    display: flex;
    align-items: center;
    padding-left: 18px;
    gap: 20px;
    color: var(--white);
    font-weight: 800;
    font-size: 27px;
    letter-spacing: 0.5px;
    line-height: 1;
  }
  .phone-icon { width: 24px; height: 24px; flex: none; }
</style>
</head>
<body>
  <section class="billboard" aria-label="Reed &amp; Vale grand opening billboard">
    <div class="green-field"></div>
    <svg class="field-edge" viewBox="0 0 880 366" aria-hidden="true">
      <line x1="358" y1="0" x2="237" y2="366" stroke="#c9cdd6" stroke-width="3"/>
    </svg>

    <div class="brand"><span class="brand-dot"></span>Reed &amp; Vale</div>
    <p class="open-dates">Open Aug 1 · <strong>Grand Opening Aug 15</strong></p>

    <div class="promo-photo" role="img" aria-label="Photo of an excited woman shouting into a red and white megaphone"></div>

    <svg class="megaphone-strokes" viewBox="0 0 42 28" aria-hidden="true">
      <polygon points="0,4 40,24 36,28" fill="#13134a"/>
      <polygon points="14,0 30,2 29,4" fill="#13134a"/>
    </svg>

    <span class="headline-script">Grand</span>
    <span class="headline-main">OPENING</span>

    <svg class="accent-strokes" viewBox="0 0 52 40" aria-hidden="true">
      <polygon points="0,36 50,4 52,8 4,40" fill="#13134a"/>
      <polygon points="10,24 24,0 26,2 14,26" fill="#13134a"/>
    </svg>

    <div class="divider"></div>

    <ul class="product-list product-list--top">
      <li>Flower</li>
      <li>Cartridges</li>
      <li>Disposables</li>
      <li>Edibles</li>
    </ul>
    <ul class="product-list product-list--bottom">
      <li>Creams</li>
      <li>Lotions</li>
      <li>Pet Products Etc</li>
    </ul>

    <div class="phone-pill">
      <svg class="phone-icon" viewBox="0 0 24 24" aria-hidden="true">
        <path fill="#ffffff" d="M6.6 10.8a15.2 15.2 0 0 0 6.6 6.6l2.2-2.2c.3-.3.7-.4 1-.2 1.1.4 2.3.6 3.6.6.6 0 1 .4 1 1V20c0 .6-.4 1-1 1A17 17 0 0 1 3 4c0-.6.4-1 1-1h3.5c.6 0 1 .4 1 1 0 1.3.2 2.5.6 3.6.1.3 0 .7-.2 1z"/>
        <path fill="none" stroke="#ffffff" stroke-width="1.6" stroke-linecap="round" d="M14 3.5a7 7 0 0 1 6.5 6.5M14 7a3.5 3.5 0 0 1 3 3"/>
      </svg>
      <span class="phone-number">+1 555-014-2290</span>
    </div>
  </section>
</body>
</html>
```